Mobility Provider needs Email Template Design

I would like to create an email template that includes our logo(designed here) and some of the services (file attached) which we provide to our customers free of charge.
I want these services visible--while I should still be able to personalized my emails...

```html
<!DOCTYPE html>
<html lang="en">
<head>
<meta charset="utf-8">
<title>MoveWise – Our Services</title>
<link rel="stylesheet" href="https://fonts.googleapis.com/css2?family=Open+Sans:wght@400;600;700&display=swap">
<style>
  :root {
    --brand-red: #c8102e;
    --brand-blue: #1f4e9e;
    --ink: #222222;
    --muted: #8a8a8a;
    --page: #f3f3f3;
    --white: #ffffff;
    --ring: #d6d6d6;
    --button-dark: #1e1e1e;
  }
  * { box-sizing: border-box; margin: 0; padding: 0; }
  html, body { width: 1200px; height: 2540px; overflow: hidden; }
  body {
    font-family: "Open Sans", Arial, sans-serif;
    background: var(--page);
    color: var(--ink);
    position: relative;
  }
  .site-header {
    height: 88px;
    background: var(--white);
    display: flex;
    align-items: center;
    justify-content: space-between;
    padding: 0 70px 0 80px;
  }
  .brand { display: flex; align-items: center; gap: 12px; }
  .brand-dot { width: 22px; height: 22px; border-radius: 50%; background: var(--brand-red); }
  .brand-name { font-size: 36px; font-weight: 700; color: var(--brand-blue); letter-spacing: -0.5px; }
  .tagline { font-size: 22px; color: #555; }

  .hero {
    position: relative;
    height: 772px;
    background: linear-gradient(100deg, #b9c3cd 0%, #e9ecef 35%, #f4f5f6 55%, #c6d3e0 80%, #9fb2c6 100%);
    text-align: center;
    overflow: hidden;
  }
  .hero-photo { position: absolute; inset: 0; }
  .hero-copy { position: relative; padding-top: 40px; }
  .hero-lead { font-size: 28px; font-weight: 700; color: var(--white); }
  .hero-title { font-size: 68px; font-weight: 400; color: var(--brand-red); line-height: 1.1; margin-top: 2px; }
  .hero-sub { font-size: 27px; font-weight: 700; color: var(--white); margin-top: 8px; }

  .services { text-align: center; padding-top: 46px; }
  .services-title { font-size: 40px; font-weight: 700; color: var(--brand-blue); letter-spacing: 1px; }
  .divider { display: flex; align-items: center; justify-content: center; gap: 10px; margin-top: 8px; }
  .divider span { width: 200px; height: 2px; background: #d9d9d9; }
  .divider i { width: 14px; height: 14px; background: var(--brand-blue); transform: rotate(45deg); }
  .services-intro { font-size: 18px; color: #444; margin-top: 12px; }

  .service-grid {
    display: grid;
    grid-template-columns: repeat(3, 300px);
    column-gap: 66px;
    padding-left: 90px;
    margin-top: 28px;
    row-gap: 105px;
  }
  .service { display: flex; flex-direction: column; align-items: center; }
  .service-icon {
    width: 296px; height: 296px; border-radius: 50%;
    background: var(--white);
    border: 10px solid var(--ring);
    display: flex; align-items: center; justify-content: center;
  }
  .service-icon svg { width: 130px; height: 130px; }
  .service-name { font-size: 20px; font-weight: 700; letter-spacing: 1px; margin-top: 34px; }
  .service-text {
    width: 236px; font-size: 20px; line-height: 28px; color: var(--muted);
    height: 112px; overflow: hidden; margin-top: 8px;
  }
  .button {
    display: inline-block; margin-top: 14px;
    width: 160px; height: 56px; line-height: 56px; border-radius: 6px;
    background: var(--brand-blue); color: var(--white);
    font-size: 20px; font-weight: 700; letter-spacing: 1px; text-decoration: none;
  }
  .button--dark { background: var(--button-dark); }

  .site-footer {
    position: absolute; left: 0; right: 0; top: 2340px;
    text-align: center;
  }
  .footer-rule { width: 1040px; height: 2px; background: #e2e2e2; margin: 0 auto; }
  .social { display: flex; justify-content: center; gap: 14px; margin-top: 56px; }
  .social span { width: 52px; height: 52px; border-radius: 50%; background: var(--brand-red); }
  .copyright { font-size: 20px; color: #c9c9c9; margin-top: 28px; }
</style>
</head>
<body>
  <header class="site-header">
    <div class="brand"><span class="brand-dot"></span><span class="brand-name">MoveWise</span></div>
    <p class="tagline">Information through mobility!</p>
  </header>

  <section class="hero">
    <div class="hero-photo" role="img" aria-label="Photo of two business people shaking hands"></div>
    <div class="hero-copy">
      <p class="hero-lead">MoveWise will provide you</p>
      <h1 class="hero-title">And your customers with</h1>
      <p class="hero-sub">The following services @ ZERO costs</p>
    </div>
  </section>

  <section class="services">
    <h2 class="services-title">OUR SERVICES</h2>
    <div class="divider"><span></span><i></i><span></span></div>
    <p class="services-intro">Find the best template for your business!</p>

    <div class="service-grid">
      <article class="service">
        <div class="service-icon">
          <svg viewBox="0 0 100 100" fill="#c8102e" stroke="#c8102e" stroke-width="4">
            <line x1="50" y1="50" x2="20" y2="25"/><line x1="50" y1="50" x2="82" y2="22"/>
            <line x1="50" y1="50" x2="15" y2="65"/><line x1="50" y1="50" x2="85" y2="62"/>
            <line x1="50" y1="50" x2="50" y2="88"/>
            <circle cx="50" cy="50" r="14"/><circle cx="20" cy="25" r="8"/><circle cx="82" cy="22" r="8"/>
            <circle cx="15" cy="65" r="7"/><circle cx="85" cy="62" r="7"/><circle cx="50" cy="88" r="8"/>
          </svg>
        </div>
        <h3 class="service-name">PROJECT MANAGEMENT</h3>
        <p class="service-text">Management: Our industry-certified Project Managers (PMP) will as your single point of</p>
        <a class="button button--dark" href="#">BUTTON</a>
      </article>

      <article class="service">
        <div class="service-icon">
          <svg viewBox="0 0 100 100" fill="#c8102e">
            <polygon points="8,14 92,14 78,32 22,32"/>
            <polygon points="22,40 78,40 68,56 32,56"/>
            <polygon points="32,64 68,64 50,92"/>
          </svg>
        </div>
        <h3 class="service-name">DEPLOYMENT SERVICES</h3>
        <p class="service-text">Your customers' needs are specific and unique. We may need to travel into uncharted territory,</p>
        <a class="button" href="#">BUTTON</a>
      </article>

      <article class="service">
        <div class="service-icon">
          <svg viewBox="0 0 100 100" fill="#c8102e" stroke="#c8102e">
            <line x1="22" y1="22" x2="80" y2="80" stroke-width="12" stroke-linecap="round"/>
            <line x1="78" y1="22" x2="22" y2="78" stroke-width="12" stroke-linecap="round"/>
            <circle cx="20" cy="20" r="13" fill="none" stroke-width="8"/>
            <circle cx="80" cy="20" r="13" fill="none" stroke-width="8"/>
            <circle cx="50" cy="50" r="12" stroke="none"/>
          </svg>
        </div>
        <h3 class="service-name">MIGRATION SERVICES</h3>
        <p class="service-text">Your customers' needs are specific and unique. We may need to travel into uncharted territory,</p>
        <a class="button" href="#">BUTTON</a>
      </article>

      <article class="service">
        <div class="service-icon">
          <svg viewBox="0 0 100 100" fill="#c8102e">
            <circle cx="30" cy="66" r="20"/>
            <rect x="62" y="12" width="18" height="10" rx="3"/>
            <path d="M60 24 h22 l-4 30 h-14 z"/>
            <rect x="68" y="54" width="6" height="30"/>
            <rect x="58" y="84" width="26" height="5" rx="2"/>
          </svg>
        </div>
        <h3 class="service-name">STAGING &amp; KITTING</h3>
        <p class="service-text">Kitting: Our staging professionals will prepare, activate, confirm device operating, install PTT</p>
        <a class="button" href="#">BUTTON</a>
      </article>

      <article class="service">
        <div class="service-icon">
          <svg viewBox="0 0 100 100" fill="#c8102e">
            <circle cx="22" cy="28" r="9"/><circle cx="50" cy="22" r="10"/><circle cx="78" cy="28" r="9"/>
            <rect x="12" y="40" width="20" height="34" rx="5"/><rect x="39" y="35" width="22" height="40" rx="5"/><rect x="68" y="40" width="20" height="34" rx="5"/>
            <rect x="15" y="72" width="6" height="20"/><rect x="23" y="72" width="6" height="20"/>
            <rect x="42" y="73" width="7" height="22"/><rect x="51" y="73" width="7" height="22"/>
            <rect x="71" y="72" width="6" height="20"/><rect x="79" y="72" width="6" height="20"/>
          </svg>
        </div>
        <h3 class="service-name">SUMMIT</h3>
        <p class="service-text">MoveWise will help manage your customers' Summit website, assisting with reports, etc.</p>
        <a class="button" href="#">BUTTON</a>
      </article>

      <article class="service">
        <div class="service-icon">
          <svg viewBox="0 0 100 100">
            <rect x="26" y="6" width="48" height="88" rx="8" fill="#c8102e"/>
            <rect x="32" y="16" width="36" height="62" fill="#ffffff"/>
            <circle cx="50" cy="86" r="4" fill="#ffffff"/>
          </svg>
        </div>
        <h3 class="service-name">FALCON</h3>
        <p class="service-text">MoveWise will complete all ordering and support services in Falcon New Activations, Ports,</p>
        <a class="button" href="#">BUTTON</a>
      </article>
    </div>
  </section>

  <footer class="site-footer">
    <div class="footer-rule"></div>
    <div class="social" aria-label="Social links"><span></span><span></span><span></span><span></span></div>
    <p class="copyright">Copyright © 2014 MoveWise</p>
  </footer>
</body>
</html>
```